Bold & Clean Brisk Harbor Stationary Design

Our company, Brisk Harbor Capital Partners needs a business card, letterhead, and envelope design that all also the formatting standards for quickleafpress.com.

Envelope:
Safe Zone: 9.375" x 4"
Trim Size: 9.5" x 4.15"
Bleed Size: 11.125" 8.625"

Letterhead:
Safe Zone: 10.875" x 8.375"
Trim Size: 11" x 8.5"
Bleed Size: 11.125" x 8.625"

Our mailing address is:
2870 W Larkhill St
Chicago, IL 60618

Please make sure the return address on the envelope is formatted correctly for mailing and the logo is not too large.

Please submit designs in word and PDF form.

Our current letterhead is attached.

We would also like a business card with our existing logo that will meet standards for formatting through Quickleaf Press (quickleafpress.com).

These standards are:
Safe Zone: 3.375" x 1.875"
Trim Size: 3.5" x 2"
Bleed Size: 3.625" x 2.125"

The business card is going to be for Marco Lindqvist, President/CEO of Brisk Harbor Capital Partners. Please include the Address, Telephone Number, Cell Phone Number, Fax Number, Email, and Website Address on the card, which are as follows:

2870 W Larkhill St
Chicago, IL 60618

Tel: (773) 555-0172
Cell: (630) 555-0138
Fax: (63) 555-0194
Email: mrl@briskharborcap.com
Web: www.briskharborcap.com

Please make sure that we can easily change the name of the staff member and job position title ourselves as we will be having cards for individual employees in the future as well.

The back of the card should also have the Brisk Harbor logo on it with our services listed:

Financial Planning | Tax | Solutions for Small Businesses

Industry/Entity Type

Accounting

Requirements
Must have
• envelope
• letterhead
• business card
• All meeting standards set out above.

```html
<!DOCTYPE html>
<html lang="en">
<head>
<meta charset="utf-8">
<title>Brisk Harbor Capital Partners – Stationery</title>
<link rel="stylesheet" href="https://fonts.googleapis.com/css2?family=Poppins:wght@400;500;600&display=swap">
<style>
  :root {
    --stage: #a9a9ab;
    --navy: #1f2d55;
    --orange: #e8502a;
    --white: #ffffff;
    --ink: #2a2f3d;
    --faint: #ecebef;
    --label: #3a3a3a;
  }
  * { box-sizing: border-box; margin: 0; padding: 0; }
  html, body { width: 1192px; height: 1200px; overflow: hidden; }
  body {
    background: var(--stage);
    font-family: "Poppins", sans-serif;
    color: var(--ink);
    position: relative;
  }
  .sheet { position: absolute; overflow: hidden; }
  .piece-label {
    position: absolute; font-size: 8px; color: var(--label);
  }

  /* brand lockup */
  .brand { display: flex; align-items: center; gap: 7px; }
  .brand-dot {
    border-radius: 50%; border: 2px solid var(--orange); flex: none;
  }
  .brand-name { font-weight: 600; color: var(--navy); white-space: nowrap; letter-spacing: .2px; }
  .brand.on-dark .brand-name { color: var(--white); }

  /* contact list */
  .contact { list-style: none; }
  .contact li { display: flex; align-items: center; gap: 6px; white-space: nowrap; }
  .contact svg { flex: none; fill: var(--orange); }

  /* business card front */
  .card-front { left: 297px; top: 42px; width: 300px; height: 171px; background: var(--white); }
  .card-front .brand { position: absolute; left: 30px; top: 18px; }
  .card-front .brand-dot { width: 22px; height: 22px; }
  .card-front .brand-name { font-size: 13px; }
  .card-person { position: absolute; right: 22px; top: 17px; text-align: left; }
  .card-person .name { color: var(--orange); font-size: 12px; font-weight: 500; line-height: 1.2; }
  .card-person .title { color: var(--ink); font-size: 10px; line-height: 1.2; }
  .card-band { position: absolute; left: 0; top: 68px; width: 100%; height: 84px; background: var(--navy); }
  .card-band .contact { position: absolute; left: 34px; top: 10px; color: var(--white); font-size: 7.5px; line-height: 13px; }
  .card-band .contact li:first-child { margin-bottom: 4px; }
  .card-circle {
    position: absolute; right: 14px; top: 118px; width: 64px; height: 64px; border-radius: 50%;
    background: var(--white); border: 3px solid var(--navy); border-right-color: var(--orange);
  }
  .card-web { position: absolute; left: 36px; bottom: 7px; color: var(--orange); font-size: 8px; font-weight: 500; }

  /* business card back */
  .card-back { left: 607px; top: 42px; width: 297px; height: 171px; background: var(--navy); }
  .card-back .brand { position: absolute; left: 58px; top: 42px; }
  .card-back .brand-dot { width: 34px; height: 34px; }
  .card-back .brand-name { font-size: 19px; }
  .services { color: var(--white); font-size: 8px; white-space: nowrap; }
  .card-back .services { position: absolute; left: 52px; top: 104px; }
  .card-back .web { position: absolute; left: 0; width: 100%; text-align: center; top: 133px; color: var(--orange); font-size: 8px; }

  /* folder cover */
  .folder { left: 97px; top: 251px; width: 500px; height: 644px; }
  .folder-photo {
    position: absolute; inset: 0;
    background:
      linear-gradient(180deg, rgba(35,45,90,.15) 0%, rgba(40,40,80,.55) 70%, rgba(55,40,75,.75) 100%),
      linear-gradient(115deg, #1b3a5e 0%, #2c5073 28%, #3b4c72 45%, #4a4a72 65%, #5c4b6e 100%);
  }
  .folder .brand { position: absolute; left: 136px; top: 470px; }
  .folder .brand-dot { width: 44px; height: 44px; }
  .folder .brand-name { font-size: 26px; }
  .folder .services { position: absolute; left: 0; width: 100%; text-align: center; top: 538px; font-size: 10.5px; }
  .folder .web { position: absolute; left: 0; width: 100%; text-align: center; top: 578px; color: var(--orange); font-size: 11px; }

  /* letterhead */
  .letterhead { left: 607px; top: 251px; width: 500px; height: 644px; background: var(--white); }
  .letterhead .brand { position: absolute; left: 48px; top: 36px; }
  .letterhead .brand-dot { width: 22px; height: 22px; }
  .letterhead .brand-name { font-size: 13px; }
  .letterhead .contact { position: absolute; left: 50px; top: 88px; font-size: 6px; line-height: 9px; color: var(--ink); }
  .ghost {
    position: absolute; display: flex; align-items: center; justify-content: center;
  }
  .ghost-ring { position: absolute; inset: 0; border-radius: 50%; border: 8px solid var(--faint); border-left-color: #e4e3e8; }
  .ghost-name { position: relative; font-weight: 600; color: var(--faint); white-space: nowrap; }
  .letterhead .ghost { left: 140px; top: 270px; width: 330px; height: 330px; }
  .letterhead .ghost-name { font-size: 44px; }
  .footer-band { position: absolute; left: 0; bottom: 0; width: 100%; height: 36px; background: var(--navy); }
  .footer-band .web { position: absolute; left: 18px; top: 11px; color: var(--white); font-size: 10px; letter-spacing: 1.5px; }
  .footer-circle {
    position: absolute; right: 4px; bottom: 2px; width: 36px; height: 36px; border-radius: 50%;
    background: var(--white); border: 2px solid var(--navy); border-right-color: var(--orange);
  }

  /* envelope front */
  .envelope-front { left: 31px; top: 931px; width: 558px; height: 244px; background: var(--white); }
  .envelope-front .brand { position: absolute; left: 30px; top: 28px; }
  .envelope-front .brand-dot { width: 18px; height: 18px; }
  .envelope-front .brand-name { font-size: 11px; }
  .return-address { position: absolute; left: 34px; top: 56px; font-size: 5.5px; line-height: 8px; color: var(--ink); }
  .envelope-front .ghost { left: 10px; top: 50px; width: 200px; height: 200px; }
  .envelope-front .ghost-name { font-size: 28px; }

  /* envelope back */
  .envelope-back { left: 599px; top: 931px; width: 558px; height: 244px; background: var(--white); }
  .flap { position: absolute; left: 0; top: 0; width: 100%; height: 78px; background: var(--navy); border-radius: 0 0 18px 18px; }
  .flap-dot { position: absolute; left: 261px; top: 22px; width: 36px; height: 36px; border-radius: 50%; border: 2px solid var(--white); }
</style>
</head>
<body>

<!-- business card front -->
<section class="sheet card-front" aria-label="Business card front">
  <div class="brand"><span class="brand-dot"></span><span class="brand-name">Brisk Harbor</span></div>
  <div class="card-person">
    <p class="name">Marco Lindqvist</p>
    <p class="title">President/CEO</p>
  </div>
  <div class="card-band">
    <ul class="contact">
      <li><svg width="6" height="8" viewBox="0 0 6 8"><path d="M3 0a3 3 0 0 0-3 3c0 2.2 3 5 3 5s3-2.8 3-5a3 3 0 0 0-3-3zm0 4.2a1.2 1.2 0 1 1 0-2.4 1.2 1.2 0 0 1 0 2.4z"/></svg>2870 W Larkhill St, Chicago, IL 60618</li>
      <li><svg width="7" height="7" viewBox="0 0 7 7"><path d="M1.4 0l1.3 1.6-.7 1a4 4 0 0 0 2.4 2.4l1-.7L7 5.6 6 7C2.7 6.8.2 4.3 0 1z"/></svg>(773) 555-0172</li>
      <li><svg width="7" height="7" viewBox="0 0 7 7"><path d="M1.4 0l1.3 1.6-.7 1a4 4 0 0 0 2.4 2.4l1-.7L7 5.6 6 7C2.7 6.8.2 4.3 0 1z"/></svg>(630) 555-0138</li>
      <li><svg width="7" height="7" viewBox="0 0 7 7"><path d="M1.4 0l1.3 1.6-.7 1a4 4 0 0 0 2.4 2.4l1-.7L7 5.6 6 7C2.7 6.8.2 4.3 0 1z"/></svg>(63) 555-0194</li>
      <li><svg width="8" height="6" viewBox="0 0 8 6"><path d="M0 0h8v6H0zm.8.8v.3L4 3.2l3.2-2.1V.8z"/></svg>mrl@briskharborcap.com</li>
    </ul>
  </div>
  <span class="card-circle"></span>
  <p class="card-web">www.briskharborcap.com</p>
</section>

<!-- business card back -->
<section class="sheet card-back" aria-label="Business card back">
  <div class="brand on-dark"><span class="brand-dot"></span><span class="brand-name">Brisk Harbor</span></div>
  <p class="services">Financial Planning | Tax | Solutions for Small Businesses</p>
  <p class="web">www.briskharborcap.com</p>
</section>

<p class="piece-label" style="left:97px;top:234px;">Letterhead Cover:</p>
<p class="piece-label" style="left:607px;top:234px;">Letterhead Paper:</p>

<!-- folder cover -->
<section class="sheet folder" aria-label="Letterhead cover">
  <div class="folder-photo" role="img" aria-label="Photo of glass city skyscrapers seen from below in blue and violet tones"></div>
  <div class="brand on-dark"><span class="brand-dot"></span><span class="brand-name">Brisk Harbor</span></div>
  <p class="services">Financial Planning | Tax | Solutions for Small Businesses</p>
  <p class="web">www.briskharborcap.com</p>
</section>

<!-- letterhead paper -->
<section class="sheet letterhead" aria-label="Letterhead paper">
  <div class="brand"><span class="brand-dot"></span><span class="brand-name">Brisk Harbor</span></div>
  <ul class="contact">
    <li><svg width="5" height="6" viewBox="0 0 6 8"><path d="M3 0a3 3 0 0 0-3 3c0 2.2 3 5 3 5s3-2.8 3-5a3 3 0 0 0-3-3z"/></svg>2870 W Larkhill St, Chicago, IL 60618</li>
    <li><svg width="5" height="5" viewBox="0 0 7 7"><path d="M1.4 0l1.3 1.6-.7 1a4 4 0 0 0 2.4 2.4l1-.7L7 5.6 6 7C2.7 6.8.2 4.3 0 1z"/></svg>(773) 555-0172</li>
    <li><svg width="5" height="5" viewBox="0 0 7 7"><path d="M1.4 0l1.3 1.6-.7 1a4 4 0 0 0 2.4 2.4l1-.7L7 5.6 6 7C2.7 6.8.2 4.3 0 1z"/></svg>(630) 555-0138</li>
    <li><svg width="5" height="5" viewBox="0 0 7 7"><path d="M1.4 0l1.3 1.6-.7 1a4 4 0 0 0 2.4 2.4l1-.7L7 5.6 6 7C2.7 6.8.2 4.3 0 1z"/></svg>(63) 555-0194</li>
    <li><svg width="6" height="5" viewBox="0 0 8 6"><path d="M0 0h8v6H0z"/></svg>mrl@briskharborcap.com</li>
  </ul>
  <div class="ghost" aria-hidden="true"><span class="ghost-ring"></span><span class="ghost-name">Brisk Harbor</span></div>
  <div class="footer-band"><p class="web">www.briskharborcap.com</p></div>
  <span class="footer-circle"></span>
</section>

<!-- envelope front -->
<section class="sheet envelope-front" aria-label="Envelope front">
  <div class="ghost" aria-hidden="true"><span class="ghost-ring"></span><span class="ghost-name">Brisk Harbor</span></div>
  <div class="brand"><span class="brand-dot"></span><span class="brand-name">Brisk Harbor</span></div>
  <p class="return-address">2870 W Larkhill St, Chicago, IL 60618</p>
  <div class="footer-band"><p class="web">www.briskharborcap.com</p></div>
  <span class="footer-circle"></span>
</section>

<!-- envelope back -->
<section class="sheet envelope-back" aria-label="Envelope back">
  <div class="flap"><span class="flap-dot"></span></div>
</section>

</body>
</html>
```